Independent manufacturing consultant needs a professional Logo & biz card Update

I want a new logo using the existing one as inspiration. The company legal name is Corvex Industrial Trade & Advisory Partners, Inc. Often the name is shortened to Corvex ITP and that matches with web address of www.corvex-itp.example. #1 create a new logo and #2 update biz card. I will need vector file to get cards printed (bilingual English & Japanese). The reverse side will be an exact copy of the original design but in Japanese. I have another resource for the translation so that is not in this scope.
Next month, a follow-up project will be to update the website using new logo and get a professional, cohesive look to all the pages.
Check out web site to get an idea of what we do. The desire is to project professional, articulate, clean, dependable, detailed oriented team of experts.

Target Market(s)

Food and Beverage manufactures. Major players, regiona, and start ups.

Industry/Entity Type

It Company

Contact Information for Business Card

exisiting card and logo provided as foundation but ready to improve upon both!

Logo Text

Corvex ITP or other....

Font styles to use
Sans Serif

Colors
9bcb3c
0356a4

Requirements
Must have
• Logo and biz card.
• Logo will be used for other materials and website.
Nice to have
• open to suggestions.
• Like the Green & Blue colors but also dig grey scale as the website incorporates.
• Open to suggestions.
Should not have
• not to animated. I work with more conservative clients.

```html
<!DOCTYPE html>
<html lang="en">
<head>
<meta charset="utf-8">
<title>Corvex ITP – Business Card</title>
<link href="https://fonts.googleapis.com/css2?family=Arimo:wght@400;700&family=Exo+2:wght@600&display=swap" rel="stylesheet">
<style>
  :root {
    --brand-blue: #0356a4;
    --brand-green: #9bcb3c;
    --card-white: #ffffff;
    --stage: #e9eaec;
    --ink-light: #ffffff;
  }
  * { box-sizing: border-box; margin: 0; padding: 0; }
  html, body {
    width: 1200px; height: 900px; overflow: hidden;
    background: var(--stage);
    font-family: "Arimo", Arial, sans-serif;
  }
  .stage {
    width: 1200px; height: 900px;
    display: flex; flex-direction: column; align-items: center; justify-content: center;
    gap: 40px;
  }
  .card {
    position: relative; width: 600px; height: 343px; overflow: hidden;
    box-shadow: 0 4px 14px rgba(0,0,0,.18);
  }

  /* Front */
  .card-front { background: var(--card-white); }
  .front-top-stripe { position: absolute; top: 0; left: 0; right: 0; height: 14px; background: var(--brand-green); }
  .front-brand {
    position: absolute; top: 58px; left: 0; right: 0; text-align: center;
  }
  .brand-wordmark {
    font-family: "Exo 2", "Arimo", sans-serif; font-weight: 600;
    font-size: 64px; letter-spacing: 3px; line-height: 1;
    color: var(--brand-blue); text-transform: uppercase;
  }
  .brand-legal {
    margin-top: 12px; font-size: 13.5px; letter-spacing: .4px;
    color: var(--brand-blue); text-transform: uppercase;
  }
  .front-contact-band {
    position: absolute; left: 0; right: 0; top: 212px; height: 74px;
    background: var(--brand-blue); color: var(--ink-light);
    display: flex; align-items: center; padding: 0 22px;
  }
  .person { width: 170px; }
  .person-name { font-size: 21px; font-weight: 700; }
  .person-title { font-size: 13px; color: var(--brand-green); margin-top: 2px; }
  .divider { width: 1px; height: 46px; background: rgba(255,255,255,.45); margin: 0 16px; }
  .contact-list { list-style: none; font-size: 12.5px; line-height: 1.7; }
  .contact-list li { display: flex; align-items: center; gap: 7px; }
  .contact-list svg { width: 12px; height: 12px; flex: none; }
  .front-address-band {
    position: absolute; left: 0; right: 0; top: 292px; height: 30px;
    background: var(--brand-green); color: var(--ink-light);
    font-size: 13px; display: flex; align-items: center; padding-left: 210px;
  }
  .front-bottom-stripe { position: absolute; left: 0; right: 0; bottom: 0; height: 14px; background: var(--brand-blue); }

  /* Back */
  .card-back {
    background: var(--brand-blue);
    display: flex; flex-direction: column; align-items: center; justify-content: center;
  }
  .card-back .brand-wordmark { color: var(--brand-green); font-size: 60px; }
  .back-web {
    margin-top: 26px; font-size: 14px; letter-spacing: 1px;
    color: var(--brand-green); text-transform: uppercase;
  }
</style>
</head>
<body>
<main class="stage">
  <section class="card card-front" aria-label="Business card front">
    <div class="front-top-stripe"></div>
    <div class="front-brand">
      <div class="brand-wordmark">Corvex ITP</div>
      <div class="brand-legal">Corvex Industrial Trade &amp; Advisory Partners, Inc</div>
    </div>
    <div class="front-contact-band">
      <div class="person">
        <div class="person-name">Daniel Okafor</div>
        <div class="person-title">Managing director</div>
      </div>
      <div class="divider"></div>
      <ul class="contact-list">
        <li><svg viewBox="0 0 12 12"><rect width="12" height="12" rx="2" fill="#fff"/><path d="M3.5 2.5l1.5 1.8-.8 1c.5 1 1.3 1.8 2.3 2.3l1-.8 1.8 1.5-.9 1.3C5.8 9.4 2.6 6.2 2.4 3.4z" fill="#0356a4"/></svg>1200-5550-1841</li>
        <li><svg viewBox="0 0 12 12"><rect width="12" height="12" rx="2" fill="#fff"/><rect x="4" y="2" width="4" height="8" rx=".8" fill="#0356a4"/></svg>0400-5550-2297</li>
      </ul>
      <div class="divider"></div>
      <ul class="contact-list">
        <li><svg viewBox="0 0 12 12"><rect width="12" height="12" rx="2" fill="#fff"/><rect x="2.5" y="3.5" width="7" height="5" fill="none" stroke="#0356a4"/><path d="M2.5 3.5L6 6.5 9.5 3.5" fill="none" stroke="#0356a4"/></svg>daniel@corvex-itp.example</li>
        <li><svg viewBox="0 0 12 12"><rect width="12" height="12" rx="2" fill="#fff"/><circle cx="6" cy="6" r="3.5" fill="none" stroke="#0356a4"/><path d="M2.5 6h7M6 2.5v7" stroke="#0356a4" stroke-width=".8"/></svg>www.corvex-itp.example</li>
      </ul>
    </div>
    <div class="front-address-band">2480 Harbor Road, Suite 210, Lakeview, OR 97000</div>
    <div class="front-bottom-stripe"></div>
  </section>

  <section class="card card-back" aria-label="Business card back">
    <div class="brand-wordmark">Corvex ITP</div>
    <div class="back-web">www.corvex-itp.example</div>
  </section>
</main>
</body>
</html>
```